Breast Cancer Car Donation Website Design

Please create a new one page website design.

Current site: http://www.givemyautohope.com/

The NEW website address will be RidesforPinkRibbonAid.org

Use these sites for an idea of what I am looking for. I like these sites best: drivesforheroesfund.org and autosforservicemen.org

```html
<!DOCTYPE html>
<html lang="en">
<head>
<meta charset="utf-8">
<title>RidesforPinkRibbonAid.org – Donate A Car Or Boat</title>
<link rel="stylesheet" href="https://fonts.googleapis.com/css2?family=Lato:wght@300;400;700&family=Marcellus&family=Tinos&display=swap">
<style>
  :root {
    --pink: #ee6f98;
    --pink-deep: #e4447f;
    --pink-soft: #f9b3cb;
    --slate: #4b5f70;
    --slate-light: #687d8e;
    --grey-text: #555d66;
    --hero-bg: #d3dbe1;
    --field-border: #8a8f96;
    --white: #ffffff;
  }
  * { box-sizing: border-box; margin: 0; padding: 0; }
  html, body { width: 1200px; height: 3614px; overflow: hidden; background: var(--white); }
  body { position: relative; font-family: "Lato", sans-serif; color: var(--grey-text); }
  .abs { position: absolute; }

  /* header */
  .account-links { left: 885px; top: 22px; font-size: 14px; color: var(--grey-text); letter-spacing: .5px; }
  .brand { left: 96px; top: 122px; display: flex; align-items: center; gap: 14px; }
  .brand-mark { width: 60px; height: 60px; background: var(--pink); }
  .brand-name { font-size: 26px; font-weight: 700; color: var(--pink); line-height: 1.1; width: 190px; }
  .header-decor { left: 398px; top: 60px; width: 735px; height: 80px; background: linear-gradient(180deg, rgba(220,226,231,0) 0%, #e6eaee 100%); }
  .main-nav { left: 398px; top: 140px; width: 735px; height: 24px; background: var(--pink); display: flex; padding-left: 160px; }
  .main-nav a { color: var(--white); text-decoration: none; font-size: 15px; letter-spacing: 2px; line-height: 24px; width: 140px; }

  /* hero */
  .hero { left: 0; top: 265px; width: 1200px; height: 270px; background: linear-gradient(90deg, #d9e0e5 0%, #c9d2d9 60%, #bfc9d1 100%); }
  .hero-photo { position: absolute; right: 0; top: 0; width: 405px; height: 270px; background: linear-gradient(90deg, #c5ced5 0%, #b4a79e 45%, #d8c2b5 75%, #e4e7ea 100%); }
  .hero-title { position: absolute; left: 234px; top: 22px; font-family: "Marcellus", serif; font-weight: 400; font-size: 96px; color: var(--pink); line-height: 1; }
  .hero-sub { position: absolute; left: 240px; top: 128px; font-size: 40px; letter-spacing: 3px; color: var(--slate); font-weight: 300; }
  .hero-cta { position: absolute; left: 238px; top: 193px; display: flex; align-items: center; gap: 20px; }
  .hero-now { background: var(--pink); color: var(--white); font-size: 18px; letter-spacing: 3px; padding: 4px 22px; }
  .hero-phone { color: var(--pink-deep); font-size: 31px; letter-spacing: 1px; }

  /* features */
  .feature { top: 588px; width: 330px; text-align: center; }
  .feature svg { display: block; margin: 0 auto 24px; }
  .feature p { font-size: 23px; line-height: 33px; color: var(--grey-text); }

  /* mission band */
  .mission { left: 0; top: 807px; width: 1200px; height: 152px; background: linear-gradient(90deg, var(--slate-light), var(--slate) 45%, #3d5060); color: var(--white); text-align: center; font-size: 19.5px; line-height: 31px; padding: 14px 140px 0; }

  /* about row */
  .about-item { display: flex; align-items: center; gap: 18px; }
  .about-item span { font-size: 24px; line-height: 32px; color: var(--grey-text); }

  /* form */
  .side-band { top: 1272px; width: 58px; height: 2198px; background: var(--pink-soft); }
  .form-title { left: 0; top: 1274px; width: 1200px; text-align: center; font-size: 33px; font-weight: 400; letter-spacing: 6px; color: var(--pink-deep); }
  .form-note { left: 0; width: 1200px; text-align: center; font-size: 17px; color: var(--grey-text); }
  .field { left: 173px; width: 854px; height: 41px; border: 1.5px solid var(--field-border); border-radius: 8px; font-family: "Tinos", serif; font-size: 19px; color: #6d7278; padding: 9px 14px; }
  .divider { left: 270px; top: 1976px; width: 660px; height: 1px; background: var(--slate-light); }
  .select { left: 173px; height: 40px; border: 1.5px solid var(--field-border); border-radius: 6px; font-family: "Tinos", serif; font-size: 18px; color: #555; padding: 8px 8px; display: flex; justify-content: space-between; align-items: center; }
  .select i { font-style: normal; font-size: 13px; color: var(--pink); }
  .field-label { left: 173px; font-size: 18px; color: var(--pink-deep); }
  .form-remark { left: 110px; top: 2806px; width: 980px; text-align: center; font-size: 16.5px; line-height: 22px; color: var(--slate); }
  .notes { left: 173px; top: 2928px; width: 854px; height: 169px; border: 1.5px solid var(--field-border); border-radius: 8px; font-family: "Tinos", serif; font-size: 19px; color: #6d7278; padding: 10px 18px; }
  .submit { left: 547px; top: 3116px; width: 106px; height: 32px; background: var(--pink); border: 2px solid var(--pink-deep); color: var(--white); font-size: 15px; letter-spacing: 2px; text-align: center; line-height: 28px; }
  .donate-bar { left: 164px; top: 3176px; width: 872px; height: 58px; background: var(--pink); border: 3px solid var(--pink-deep); color: var(--white); text-align: center; font-size: 34px; letter-spacing: 8px; line-height: 52px; }
  .screening-ad { left: 494px; top: 3278px; width: 198px; height: 125px; background: linear-gradient(135deg, #f4d4dc 0%, #e8eef4 55%, #9fd8f0 100%); }

  /* footer */
  .footer-link { left: 0; top: 3515px; width: 1200px; text-align: center; font-size: 13px; color: var(--grey-text); }
  .footer-rule { left: 518px; top: 3538px; width: 164px; height: 1px; background: var(--grey-text); }
  .footer-text { left: 100px; top: 3544px; width: 1000px; text-align: center; font-size: 11.5px; line-height: 17px; color: var(--grey-text); }
</style>
</head>
<body>

<header>
  <div class="abs account-links">Login / Register</div>
  <div class="abs brand">
    <div class="brand-mark"></div>
    <div class="brand-name">Pink Ribbon Aid Alliance</div>
  </div>
  <div class="abs header-decor" role="img" aria-label="Decorative header sweep"></div>
  <nav class="abs main-nav">
    <a href="#">ABOUT</a>
    <a href="#">CONTACT</a>
    <a href="#">FAQ</a>
  </nav>
</header>

<section class="abs hero">
  <div class="hero-photo" role="img" aria-label="Portrait of a smiling woman supporter"></div>
  <h1 class="hero-title">Donate</h1>
  <div class="hero-sub">A Car Or Boat</div>
  <div class="hero-cta">
    <span class="hero-now">NOW</span>
    <span class="hero-phone">888-555-0142</span>
  </div>
</section>

<section>
  <div class="abs feature" style="left:64px">
    <svg width="60" height="60" viewBox="0 0 24 24" aria-hidden="true">
      <path fill="#ee6f98" d="M6.6 10.8a15.1 15.1 0 0 0 6.6 6.6l2.2-2.2c.3-.3.7-.4 1-.2 1.1.4 2.3.6 3.6.6.6 0 1 .4 1 1V20c0 .6-.4 1-1 1A17 17 0 0 1 3 4c0-.6.4-1 1-1h3.5c.6 0 1 .4 1 1 0 1.3.2 2.5.6 3.6.1.3 0 .7-.2 1z"/>
    </svg>
    <p>Fast Free Pickup<br>24hr Response</p>
  </div>
  <div class="abs feature" style="left:406px">
    <svg width="84" height="62" viewBox="0 0 84 62" aria-hidden="true" fill="none" stroke="#ee6f98" stroke-width="4" stroke-linejoin="round" stroke-linecap="round">
      <path d="M14 24c2-12 16-18 32-16 12 1 22 8 24 16h6v12h-6c-2 6-6 10-10 12v8h-8v-6H30v6h-8v-8c-6-3-10-8-10-14H6v-10z"/>
      <path d="M32 30l8 8 16-18"/>
    </svg>
    <p>Tax Deduction<br>Easy To Do!</p>
  </div>
  <div class="abs feature" style="left:787px">
    <svg width="90" height="60" viewBox="0 0 90 60" aria-hidden="true" fill="none" stroke="#ee6f98" stroke-width="4" stroke-linecap="round">
      <path d="M12 22c12 22 54 22 66 0"/>
      <path d="M6 16l6 6 8-4"/>
      <path d="M84 16l-6 6-8-4"/>
    </svg>
    <p>Running or not<br>No Emission Test Required</p>
  </div>
</section>

<section class="abs mission">
  Your car or boat donation helps support those stricken by breast cancer &amp; their families, and supports programs for screening, prevention, treatment and patient well being. Our operators are standing by 24 hours a day, 7 days a week to answer your questions and get your car or boat donation picked up quickly!
</section>

<section>
  <div class="abs about-item" style="left:72px;top:1060px">
    <svg width="128" height="80" viewBox="0 0 128 80" aria-hidden="true">
      <path fill="#ee6f98" d="M6 58V40c0-6 4-10 10-11l14-3 14-18c2-3 6-5 10-5h30c5 0 9 3 12 7l12 17c8 1 14 6 14 13v18z"/>
      <path fill="#fff" d="M50 12h16v16H38zM72 12h12c3 0 5 1 7 3l9 13H72z"/>
      <circle cx="32" cy="60" r="13" fill="#ee6f98" stroke="#fff" stroke-width="4"/>
      <circle cx="98" cy="60" r="13" fill="#ee6f98" stroke="#fff" stroke-width="4"/>
    </svg>
    <span>About<br>Donating A Car</span>
  </div>
  <div class="abs about-item" style="left:462px;top:1052px">
    <div style="width:54px;height:54px;border-radius:50%;background:var(--pink)"></div>
    <span>About<br>Breast Cancer</span>
  </div>
  <div class="abs about-item" style="left:770px;top:1048px">
    <div style="width:104px;height:90px;background:var(--pink)"></div>
    <span>About<br>Pink Ribbon Aid<br>Alliance</span>
  </div>
</section>

<section>
  <div class="abs side-band" style="left:0"></div>
  <div class="abs side-band" style="left:1144px"></div>

  <h2 class="abs form-title">DONOR INFORMATION</h2>
  <p class="abs form-note" style="top:1320px">Please fill out this form and we'll schedule you for a pick up right away.</p>

  <div class="abs field" style="top:1366px">First Name</div>
  <div class="abs field" style="top:1418px">Last Name</div>
  <div class="abs field" style="top:1470px">Street Address</div>
  <div class="abs field" style="top:1522px">City</div>
  <div class="abs field" style="top:1574px">State</div>
  <div class="abs field" style="top:1626px">Zip</div>

  <p class="abs form-note" style="top:1698px">If your vehicle is at a different location, please provide detailed information:</p>

  <div class="abs field" style="top:1745px">Pick-Up Steet Address</div>
  <div class="abs field" style="top:1797px">Pick-Up City</div>
  <div class="abs field" style="top:1849px">Pick-Up State</div>
  <div class="abs field" style="top:1901px">Pick-Up Zip Code</div>

  <div class="abs divider"></div>

  <div class="abs field" style="top:2015px">E-mail Address</div>
  <div class="abs field" style="top:2067px">Day Phone</div>
  <div class="abs field" style="top:2119px">Cell Phone</div>
  <div class="abs field" style="top:2171px">Evening Phone</div>
  <div class="abs field" style="top:2223px">Vehicle Year</div>
  <div class="abs field" style="top:2275px">Vehicle Make</div>
  <div class="abs field" style="top:2327px">Vehicle Color</div>
  <div class="abs field" style="top:2379px">Vin (If is available)</div>
  <div class="abs field" style="top:2431px">Mileage</div>
  <div class="abs field" style="top:2483px">Pick-Up Zip Code</div>

  <div class="abs select" style="top:2530px;width:104px">Running <i>&#9662;</i></div>
  <div class="abs field-label" style="top:2594px">Major Body Damage:</div>
  <div class="abs select" style="top:2634px;width:82px">Yes <i>&#9662;</i></div>
  <div class="abs field-label" style="top:2692px">Do you have title?:</div>
  <div class="abs select" style="top:2724px;width:82px">Yes <i>&#9662;</i></div>

  <p class="abs form-remark">We can accept cars with no title and/or in poor condition, but we may choose to send those to a different company for pickup. Any information you can provide to help us make that decision would be appreciated. If your older vehicle has exceptional low mileage or might be considered a "Classic," please let us know that also!</p>

  <div class="abs notes">Notes of Questions</div>
  <div class="abs submit">SUBMIT</div>
  <div class="abs donate-bar">DONATE NOW</div>
  <div class="abs screening-ad" role="img" aria-label="Free breast cancer screening promotion banner"></div>
</section>

<footer>
  <div class="abs footer-link">Privacy Policy</div>
  <div class="abs footer-rule"></div>
  <p class="abs footer-text">Pink Ribbon Aid Alliance is a 501(c)(3) non-profit organization in full accordance with all laws and regulations of the US Government and the IRS. Your donation is tax deductible in<br>accordance with Federal regulations.<br>© Pink Ribbon Aid Alliance 2016. All Rights Reserved</p>
</footer>

</body>
</html>
```